Simple Clean Menu for 'Toasty Biscuits & Batter'!!!!

We are needing a menu for a cookie & cookie dough shop in the Philadelphia PA area called 'Toasty' We make delicious edible cookie doughs and warm cookies.

Attached to the project is the following
1.  The menu content and pricing
2.  A competitors menu (we want it to look better than theirs!)
3.  Our logo
4. Some Images of what we serve so you better understand.
5. A hand drawn sketch we made (keep in mind we do not want a vertical menu... its just to help get your mind going)

We want the menu to be horizontal and the sections should be divided in columns from left to right not top to bottom. Column 1 - cookie dough section(with toppings at the bottom), Column 2 (or 2+3)- Gourmet cookie and signature cookie column, Column 3 (or 4) -bakedwiches and drinks

We would like custom icon designs for the dough with 1,2,3 scoops - (refer to drawings) for the cookies (not necessarily every flavor), and definitely for the bakedwiches.

The dimensions of our in store sign will be 29.75 inches h x 69.5 inches w horizontal and it will be hanging on the wall and we need all source files and infinitely scalable photoshop pdf and of course follow a lighter color scheme according to our logo etc.

Industry/Entity Type

Shop

Font styles to use
Sans Serif
Other font styles liked:
• Refer to Description + Documents

Requirements
Must have
Nice to have
Should not have

```html
<!DOCTYPE html>
<html lang="en">
<head>
<meta charset="utf-8">
<title>Toasty Biscuits &amp; Batter – Menu Board</title>
<link rel="stylesheet" href="https://fonts.googleapis.com/css2?family=Roboto+Condensed:wght@300;400;700&display=swap">
<style>
  :root {
    --page: #eef1f5;
    --frame: #3b3b3b;
    --sky: #3cc3e6;
    --dough: #f0ad45;
    --gourmet: #ee4f97;
    --signature: #f07cb0;
    --wich: #38c2e4;
    --drinks: #1fa3e0;
    --white: #ffffff;
    --ink: #2e2e2e;
    --choc: #5a2e12;
    --tan: #c99a63;
    --caramel: #e7a23b;
    --pink-dough: #f5a3c4;
    --mint: #3aa34a;
    --red: #c8102e;
    --yellow: #f7e12b;
  }
  * { box-sizing: border-box; margin: 0; padding: 0; }
  html, body { width: 1200px; height: 825px; overflow: hidden; }
  body {
    background: var(--page);
    font-family: "Roboto Condensed", "Arial Narrow", sans-serif;
    color: var(--white);
    position: relative;
  }
  .menu-board {
    position: absolute; left: 30px; top: 168px;
    width: 1140px; height: 488px;
    background: var(--frame);
    padding: 8px;
    display: grid;
    grid-template-columns: 262px 250px 226px 205px 157px;
    gap: 6px;
  }
  .column { display: flex; flex-direction: column; gap: 6px; min-height: 0; }
  .brand-column .sky-panel { background: var(--sky); }
  .brand-column .sky-top { flex: 0 0 218px; }
  .brand-column .sky-bottom { flex: 1; }
  .brand-panel {
    flex: 0 0 110px; background: var(--white);
    display: flex; align-items: center; justify-content: center; gap: 12px;
  }
  .brand-dot { width: 40px; height: 40px; border-radius: 50%; background: var(--dough); }
  .brand-name { font-size: 46px; font-weight: 700; color: var(--ink); letter-spacing: -0.5px; }

  .section-head {
    flex: 0 0 80px; display: flex; align-items: center; justify-content: space-between;
    padding: 0 14px 0 18px; gap: 6px;
  }
  .section-title { font-size: 21px; font-weight: 700; line-height: 1.1; }
  .section-body { flex: 1; padding: 14px 14px 10px; display: flex; flex-direction: column; }
  .intro { font-size: 9.5px; font-weight: 300; line-height: 1.35; }

  .dough .section-head, .dough .section-body { background: var(--dough); }
  .gourmet .section-head, .gourmet .section-body { background: var(--gourmet); }
  .signature .section-head, .signature .section-body { background: var(--signature); }
  .wiches .section-head, .wiches .section-body { background: var(--wich); }

  .option-row { display: flex; justify-content: space-around; align-items: flex-end; text-align: center; }
  .option { display: flex; flex-direction: column; align-items: center; gap: 4px; }
  .option-label { font-size: 9px; font-weight: 300; line-height: 1.15; }
  .option-price { font-size: 9.5px; font-weight: 700; }
  .sizes { margin-top: 34px; }
  .addon-title { margin-top: 40px; text-align: center; font-size: 12px; font-weight: 700; }
  .addons { margin-top: 18px; }
  .addons .option-label { font-weight: 400; }

  .counts { margin-top: 14px; }
  .flavor-grid {
    margin-top: 22px; display: grid; grid-template-columns: repeat(3, 1fr);
    row-gap: 16px; text-align: center;
  }
  .flavor { display: flex; flex-direction: column; align-items: center; gap: 5px; }
  .flavor-name { font-size: 9px; font-weight: 400; line-height: 1.15; }
  .signature .counts { margin-top: 20px; }
  .signature .flavor-grid { margin-top: 22px; }
  .flavor-grid.pair { grid-template-columns: repeat(2, 1fr); padding: 0 18px; }
  .signature .flavor-grid + .flavor-grid { margin-top: 14px; }

  .wich-grid {
    display: grid; grid-template-columns: 1fr 1fr; column-gap: 8px; row-gap: 10px;
    text-align: center;
  }
  .wiches .section-body { padding: 12px 8px 8px; flex: 0 0 292px; }
  .wich-item { display: flex; flex-direction: column; align-items: center; }
  .wich-name { font-size: 8px; font-weight: 700; line-height: 1.2; margin-top: 4px; }
  .wich-price { font-size: 8px; font-weight: 700; }
  .wich-desc { font-size: 7px; font-weight: 300; line-height: 1.25; margin-top: 2px; }
  .drinks-panel {
    flex: 1; background: var(--drinks); display: flex; align-items: center; gap: 7px; padding: 0 8px;
  }
  .drinks-title { font-size: 15px; font-weight: 700; }
  .drinks-list { list-style: none; font-size: 7.5px; font-weight: 300; line-height: 1.35; white-space: nowrap; }
  .drinks-list b { font-weight: 700; }
  svg { display: block; flex-shrink: 0; }
</style>
</head>
<body>

<svg width="0" height="0" style="position:absolute">
  <defs>
    <symbol id="cookie" viewBox="0 0 24 24">
      <circle cx="12" cy="12" r="10.5" fill="none" stroke="#fff" stroke-width="1.4"/>
      <circle cx="8" cy="9" r="0.9" fill="#fff"/><circle cx="14" cy="7.5" r="0.9" fill="#fff"/>
      <circle cx="15" cy="14" r="0.9" fill="#fff"/><circle cx="9" cy="15.5" r="0.9" fill="#fff"/>
    </symbol>
    <symbol id="sandwich" viewBox="0 0 24 24">
      <circle cx="12" cy="12" r="10" fill="none" stroke="#fff" stroke-width="1.2"/>
      <circle cx="14" cy="12" r="10" fill="none" stroke="#fff" stroke-width="1.2"/>
      <circle cx="9" cy="9" r="0.9" fill="#fff"/><circle cx="12" cy="14" r="0.9" fill="#fff"/>
    </symbol>
  </defs>
</svg>

<main class="menu-board">

  <section class="column brand-column">
    <div class="sky-panel sky-top" role="img" aria-label="Light blue polka-dot pattern"></div>
    <div class="brand-panel">
      <span class="brand-dot"></span>
      <span class="brand-name">Toasty</span>
    </div>
    <div class="sky-panel sky-bottom" role="img" aria-label="Light blue polka-dot pattern"></div>
  </section>

  <section class="column dough">
    <header class="section-head">
      <h2 class="section-title">Gourmet<br>Cookie<br>Dough!</h2>
      <svg width="54" height="54" viewBox="0 0 54 54"><circle cx="27" cy="27" r="25" fill="none" stroke="#fff" stroke-width="2"/></svg>
    </header>
    <div class="section-body">
      <p class="intro">Try our many flavors of delicious edible cookie dough. Our dough tastes just like it should so you'll never know it's egg free and completely safe to eat! In a cone, in a cup, warm or cold there's no wrong way to eat our dough.</p>
      <div class="option-row sizes">
        <div class="option">
          <svg width="26" height="40" viewBox="0 0 26 40"><circle cx="13" cy="13" r="9" fill="none" stroke="#fff" stroke-width="1.4"/><path d="M4 20 L7 36 H19 L22 20 Z" fill="var(--dough)" stroke="#fff" stroke-width="1.4"/></svg>
          <span class="option-label">Small</span><span class="option-price">$4</span>
        </div>
        <div class="option">
          <svg width="32" height="40" viewBox="0 0 32 40"><circle cx="11" cy="13" r="8" fill="none" stroke="#fff" stroke-width="1.4"/><circle cx="20" cy="13" r="8" fill="var(--dough)" stroke="#fff" stroke-width="1.4"/><path d="M4 20 L7 36 H25 L28 20 Z" fill="var(--dough)" stroke="#fff" stroke-width="1.4"/></svg>
          <span class="option-label">Medium</span><span class="option-price">$7</span>
        </div>
        <div class="option">
          <svg width="36" height="48" viewBox="0 0 36 48"><circle cx="18" cy="10" r="8" fill="none" stroke="#fff" stroke-width="1.4"/><circle cx="11" cy="20" r="8" fill="var(--dough)" stroke="#fff" stroke-width="1.4"/><circle cx="24" cy="20" r="8" fill="var(--dough)" stroke="#fff" stroke-width="1.4"/><path d="M4 27 L7 44 H29 L32 27 Z" fill="var(--dough)" stroke="#fff" stroke-width="1.4"/></svg>
          <span class="option-label">Large</span><span class="option-price">$9</span>
        </div>
        <div class="option">
          <svg width="24" height="30" viewBox="0 0 24 30"><path d="M2 6 H22 L12 28 Z" fill="none" stroke="#fff" stroke-width="1.4"/></svg>
          <span class="option-label">In a cone</span><span class="option-price">+ $1</span>
        </div>
      </div>
      <p class="addon-title">Add for $0.50 each:</p>
      <div class="option-row addons">
        <div class="option">
          <svg width="30" height="24" viewBox="0 0 30 24"><path d="M3 21 Q3 8 13 6 Q17 2 21 6 Q27 9 27 21 Z" fill="#fff"/></svg>
          <span class="option-label">Marsh-<br>mallow</span>
        </div>
        <div class="option">
          <svg width="30" height="24" viewBox="0 0 30 24"><path d="M3 21 Q3 8 13 6 Q17 2 21 6 Q27 9 27 21 Z" fill="none" stroke="#fff" stroke-width="1.4"/></svg>
          <span class="option-label">Caramel</span>
        </div>
        <div class="option">
          <svg width="30" height="24" viewBox="0 0 30 24"><path d="M3 21 Q3 8 13 6 Q17 2 21 6 Q27 9 27 21 Z" fill="var(--choc)" stroke="#fff" stroke-width="1.4"/></svg>
          <span class="option-label">Chocolate<br>Syrup</span>
        </div>
        <div class="option">
          <svg width="30" height="24" viewBox="0 0 30 24"><path d="M3 21 Q3 8 10 9 Q12 2 19 4 Q27 7 27 21 Z" fill="#fff"/></svg>
          <span class="option-label">Whipped<br>Cream</span>
        </div>
      </div>
    </div>
  </section>

  <section class="column gourmet">
    <header class="section-head">
      <h2 class="section-title">Gourmet<br>Cookies</h2>
      <svg width="54" height="54"><use href="#cookie"/></svg>
    </header>
    <div class="section-body">
      <div class="option-row counts">
        <div class="option"><svg width="24" height="24"><use href="#cookie"/></svg><span class="option-label">1 unit</span><span class="option-price">$1.50</span></div>
        <div class="option"><svg width="44" height="40" viewBox="0 0 44 40"><use href="#cookie" x="0" y="0" width="22" height="22"/><use href="#cookie" x="11" y="0" width="22" height="22"/><use href="#cookie" x="22" y="0" width="22" height="22"/><use href="#cookie" x="5" y="16" width="22" height="22"/><use href="#cookie" x="17" y="16" width="22" height="22"/></svg><span class="option-label">6 units</span><span class="option-price">$8</span></div>
        <div class="option"><svg width="54" height="44" viewBox="0 0 54 44"><use href="#cookie" x="0" y="0" width="20" height="20"/><use href="#cookie" x="11" y="0" width="20" height="20"/><use href="#cookie" x="22" y="0" width="20" height="20"/><use href="#cookie" x="33" y="0" width="20" height="20"/><use href="#cookie" x="0" y="12" width="20" height="20"/><use href="#cookie" x="17" y="12" width="20" height="20"/><use href="#cookie" x="33" y="12" width="20" height="20"/><use href="#cookie" x="5" y="23" width="20" height="20"/><use href="#cookie" x="28" y="23" width="20" height="20"/></svg><span class="option-label">12 units</span><span class="option-price">$15</span></div>
      </div>
      <div class="flavor-grid">
        <div class="flavor"><svg width="28" height="28"><circle cx="14" cy="14" r="13" fill="var(--choc)"/></svg><span class="flavor-name">Chocolate<br>Chip</span></div>
        <div class="flavor"><svg width="28" height="28" viewBox="0 0 28 28"><circle cx="14" cy="14" r="13" fill="var(--choc)"/><path d="M24 5 A13 13 0 0 1 10 26 Z" fill="var(--gourmet)"/></svg><span class="flavor-name">Gluten Free<br>Chocolate Chip</span></div>
        <div class="flavor"></div>
        <div class="flavor"><svg width="28" height="28"><circle cx="14" cy="14" r="13" fill="var(--tan)"/></svg><span class="flavor-name">Oatmeal<br>Raisin</span></div>
        <div class="flavor"><svg width="28" height="28" viewBox="0 0 28 28"><circle cx="14" cy="14" r="13" fill="#fff"/><path d="M24 5 A13 13 0 0 1 10 26 Z" fill="var(--caramel)"/></svg><span class="flavor-name">White Chocolate<br>Macadamia</span></div>
        <div class="flavor"><svg width="28" height="28" viewBox="0 0 28 28"><circle cx="14" cy="14" r="13" fill="var(--tan)"/><path d="M24 5 A13 13 0 0 1 10 26 Z" fill="var(--choc)"/></svg><span class="flavor-name">Toffee Bar<br>Crunch</span></div>
        <div class="flavor"><svg width="28" height="28" viewBox="0 0 28 28"><circle cx="14" cy="14" r="13" fill="var(--sky)"/><path d="M24 5 A13 13 0 0 1 10 26 Z" fill="var(--yellow)"/></svg><span class="flavor-name">Candy Button</span></div>
        <div class="flavor"><svg width="28" height="28"><circle cx="14" cy="14" r="13" fill="#fff"/></svg><span class="flavor-name">Sugar</span></div>
        <div class="flavor"><svg width="28" height="28" viewBox="0 0 28 28"><circle cx="14" cy="14" r="13" fill="var(--red)"/><path d="M24 5 A13 13 0 0 1 10 26 Z" fill="#fff"/></svg><span class="flavor-name">Red Velvet</span></div>
      </div>
    </div>
  </section>

  <section class="column signature">
    <header class="section-head">
      <h2 class="section-title">Toasty<br>Signature<br>Cookies</h2>
      <svg width="48" height="48"><use href="#cookie"/></svg>
    </header>
    <div class="section-body">
      <p class="intro">Our most decadent, gourmet cookies. 100% GMO Free, Free from Artificial colors and flavorings and made with milk, cream and butter from happy hormone free cows!</p>
      <div class="option-row counts">
        <div class="option"><svg width="22" height="22"><use href="#cookie"/></svg><span class="option-label">1 unit</span><span class="option-price">$3</span></div>
        <div class="option"><svg width="40" height="36" viewBox="0 0 44 40"><use href="#cookie" x="0" y="0" width="22" height="22"/><use href="#cookie" x="11" y="0" width="22" height="22"/><use href="#cookie" x="22" y="0" width="22" height="22"/><use href="#cookie" x="5" y="16" width="22" height="22"/><use href="#cookie" x="17" y="16" width="22" height="22"/></svg><span class="option-label">6 units</span><span class="option-price">$16</span></div>
        <div class="option"><svg width="48" height="40" viewBox="0 0 54 44"><use href="#cookie" x="0" y="0" width="20" height="20"/><use href="#cookie" x="11" y="0" width="20" height="20"/><use href="#cookie" x="22" y="0" width="20" height="20"/><use href="#cookie" x="33" y="0" width="20" height="20"/><use href="#cookie" x="0" y="12" width="20" height="20"/><use href="#cookie" x="17" y="12" width="20" height="20"/><use href="#cookie" x="33" y="12" width="20" height="20"/><use href="#cookie" x="5" y="23" width="20" height="20"/><use href="#cookie" x="28" y="23" width="20" height="20"/></svg><span class="option-label">12 units</span><span class="option-price">$30</span></div>
      </div>
      <div class="flavor-grid pair">
        <div class="flavor"><svg width="26" height="26"><circle cx="13" cy="13" r="12" fill="var(--choc)"/></svg><span class="flavor-name">Chocolate<br>Chunk</span></div>
        <div class="flavor"><svg width="26" height="26"><circle cx="13" cy="13" r="12" fill="var(--tan)"/></svg><span class="flavor-name">Snickerdoodle</span></div>
      </div>
      <div class="flavor-grid">
        <div class="flavor"><svg width="26" height="26"><circle cx="13" cy="13" r="12" fill="var(--mint)"/></svg><span class="flavor-name">Lemon<br>Blueberry</span></div>
        <div class="flavor"><svg width="26" height="26"><circle cx="13" cy="13" r="12" fill="var(--caramel)"/></svg><span class="flavor-name">Salted<br>Caramel</span></div>
        <div class="flavor"><svg width="26" height="26"><circle cx="13" cy="13" r="12" fill="var(--caramel)"/></svg><span class="flavor-name">Peanut<br>Butter</span></div>
      </div>
    </div>
  </section>

  <section class="column wiches">
    <header class="section-head">
      <h2 class="section-title" style="font-size:19px">Toasty-<br>wiches</h2>
      <svg width="46" height="46"><use href="#sandwich"/></svg>
    </header>
    <div class="section-body">
      <div class="wich-grid">
        <div class="wich-item">
          <svg width="26" height="26" viewBox="0 0 26 26"><circle cx="13" cy="13" r="12" fill="var(--gourmet)"/><rect x="9" y="2" width="8" height="22" fill="var(--caramel)"/></svg>
          <span class="wich-name">The "Un-Toastywich"</span><span class="wich-price">$6</span>
          <span class="wich-desc">Any flavor of our delicious cookie dough stuffed between your choice of two Gourmet Cookies!</span>
        </div>
        <div class="wich-item">
          <svg width="26" height="26" viewBox="0 0 26 26"><circle cx="13" cy="13" r="12" fill="var(--gourmet)"/><rect x="9" y="2" width="8" height="22" fill="#fff"/></svg>
          <span class="wich-name">The Ice Cream Toastywich</span><span class="wich-price">$5</span>
          <span class="wich-desc">Creamy vanilla ice cream stuffed between your choice of any two Gourmet Cookies!</span>
        </div>
        <div class="wich-item">
          <svg width="26" height="26" viewBox="0 0 26 26"><circle cx="13" cy="13" r="12" fill="var(--choc)"/><rect x="9" y="2" width="8" height="22" fill="#fff"/></svg>
          <span class="wich-name">The Ice Cream Doughwich</span><span class="wich-price">$6</span>
          <span class="wich-desc">Creamy vanilla ice cream stuffed between delicious chocolate chip cookie dough, nuff said</span>
        </div>
        <div class="wich-item">
          <svg width="26" height="26" viewBox="0 0 26 26"><circle cx="13" cy="13" r="12" fill="var(--pink-dough)"/><rect x="9" y="2" width="8" height="22" fill="var(--caramel)"/></svg>
          <span class="wich-name">Signature Upgrade</span><span class="wich-price">$2.50</span>
          <span class="wich-desc">Make any Toastywich with any two Signature Cookies for just $2.50!</span>
        </div>
      </div>
    </div>
    <div class="drinks-panel">
      <h2 class="drinks-title">Drinks</h2>
      <ul class="drinks-list">
        <li>Water: <b>$2.25</b></li>
        <li>Organic Chocolate Milk: <b>$3</b></li>
        <li>Organic Milk: <b>$3</b></li>
      </ul>
    </div>
  </section>

</main>
</body>
</html>
```